タイトルのバランスが良く、視認性が高かったので採用いたしました。
この度はデザインをご提案いただきありがとうございました。
今後も同様のお仕事を発注してまいりますので、また機会がありましたらよろしくお願いいたします。
YouTubeのサムネイル制作/ラピトル バナー作成の仕事の依頼
バンコクで旅行会社を運営しています。
旅行業をやりながらYouTubeチャンネルやブログをやっていますので、サムネイルなどの発注が主になります。

```html
<!DOCTYPE html>
<html lang="ja">
<head>
<meta charset="utf-8">
<title>ターク県ラピトルの麺野郎</title>
<link rel="stylesheet" href="https://fonts.googleapis.com/css2?family=M+PLUS+Rounded+1c:wght@800&family=Yuji+Boku&display=swap">
<style>
  :root {
    --title-fill: #ffffff;
    --title-edge: #1c2fd6;
    --accent-red: #e0141c;
    --ink: #111111;
    --paper: #f1dfb6;
    --paper-edge: #8a5a2b;
    --photo-warm: #8a5a3a;
    --photo-dark: #2b231d;
    --photo-red: #b3322c;
  }
  html, body {
    margin: 0;
    padding: 0;
    width: 1200px;
    height: 692px;
    overflow: hidden;
    background: #000;
  }
  .thumbnail {
    position: relative;
    width: 1200px;
    height: 692px;
    overflow: hidden;
  }
  .scene-photo {
    position: absolute;
    inset: 0;
    background:
      radial-gradient(ellipse 380px 300px at 600px 420px, #3f5a4a 0%, rgba(63,90,74,0) 70%),
      radial-gradient(ellipse 300px 160px at 620px 660px, #e9e2d4 0%, rgba(233,226,212,0) 70%),
      radial-gradient(ellipse 260px 200px at 1060px 560px, var(--photo-red) 0%, rgba(179,50,44,0) 70%),
      linear-gradient(180deg, var(--photo-dark) 0%, var(--photo-warm) 45%, #6b4a35 100%);
  }
  .title-line {
    position: absolute;
    left: 14px;
    top: 12px;
    margin: 0;
    font-family: "M PLUS Rounded 1c", sans-serif;
    font-weight: 800;
    font-size: 104px;
    line-height: 1;
    letter-spacing: -2px;
    color: var(--title-fill);
    -webkit-text-stroke: 16px var(--title-edge);
    paint-order: stroke fill;
    white-space: nowrap;
  }
  .title-particle {
    position: absolute;
    left: 1052px;
    top: 40px;
    font-family: "M PLUS Rounded 1c", sans-serif;
    font-weight: 800;
    font-size: 104px;
    line-height: 1;
    color: var(--accent-red);
    -webkit-text-stroke: 14px var(--title-fill);
    paint-order: stroke fill;
  }
  .region-tag {
    position: absolute;
    left: 850px;
    top: 150px;
    width: 300px;
    height: 150px;
    transform: rotate(8deg);
    background: var(--paper);
    border: 4px solid var(--paper-edge);
    border-radius: 14px;
    display: flex;
    align-items: center;
    justify-content: center;
    font-family: "M PLUS Rounded 1c", sans-serif;
    font-weight: 800;
    font-size: 58px;
    color: var(--accent-red);
  }
  .headline-main {
    position: absolute;
    left: 10px;
    top: 230px;
    margin: 0;
    font-family: "Yuji Boku", serif;
    font-size: 420px;
    line-height: 1;
    color: var(--title-fill);
    -webkit-text-stroke: 18px var(--ink);
    paint-order: stroke fill;
  }
  .headline-sub {
    position: absolute;
    left: 760px;
    top: 400px;
    font-family: "Yuji Boku", serif;
    font-size: 200px;
    line-height: 1;
    letter-spacing: 12px;
    color: var(--ink);
    -webkit-text-stroke: 14px var(--title-fill);
    paint-order: stroke fill;
    white-space: nowrap;
  }
</style>
</head>
<body>
  <div class="thumbnail">
    <div class="scene-photo" role="img" aria-label="タイ北部の食堂で、眼鏡をかけた男性が丼から麺を箸ですくって大きく口を開けて食べている写真"></div>
    <h1 class="title-line">ターク県ラピトル</h1>
    <span class="title-particle">の</span>
    <div class="region-tag">タイ北部</div>
    <p class="headline-main">麺</p>
    <span class="headline-sub">野郎</span>
  </div>
</body>
</html>
```